Tavolin brise

i am a designer who works with home-based business. i want to give surprise to my sister with describing a luxurious display at her blog.
two days later she would be birthday

Business

```html
<!DOCTYPE html>
<html lang="en">
<head>
<meta charset="utf-8">
<title>Tavolin brise</title>
<link rel="stylesheet" href="https://fonts.googleapis.com/css2?family=Ubuntu:wght@400;500&family=Arimo:wght@400;700&family=Pinyon+Script&display=swap">
<style>
:root{
  --night:#151414;
  --night-pattern:#1f1e1d;
  --orange:#e27d1f;
  --orange-deep:#c9600f;
  --orange-light:#f29a3a;
  --paper:#f6c978;
  --paper-dark:#e9a94e;
  --heading:#b5520f;
  --link-red:#8b1a0a;
  --ink:#1a1a1a;
  --body-text:#444;
  --white:#ffffff;
  --rule:#8a8a8a;
}
*{box-sizing:border-box;margin:0;padding:0}
html,body{width:819px;height:1200px;overflow:hidden}
body{
  position:relative;
  background:radial-gradient(circle at 50% 40%,var(--night-pattern),var(--night) 70%);
  font-family:"Arimo",Arial,sans-serif;
  color:var(--ink);
}
.abs{position:absolute}

/* header */
.social{top:13px;left:623px;display:flex;gap:8px}
.social span{width:19px;height:19px;border-radius:50%;background:#3a7bd5;display:block}
.social span:nth-child(2){background:#3fa9e0}
.social span:nth-child(3){background:#1f6fb2;border-radius:3px}
.social span:nth-child(4){background:#e8e8e8;border-radius:3px}
.social span:nth-child(5){background:#f07a1a;border-radius:3px}
.brand{top:50px;left:88px;font-family:"Ubuntu",sans-serif;font-weight:500;font-size:42px;color:var(--orange-light);letter-spacing:.5px}

.login{top:47px;left:497px;width:266px;height:100px;border-radius:4px 4px 0 0;
  background:linear-gradient(160deg,var(--paper),#f0b964 60%,var(--paper-dark))}
.login-title{top:6px;left:0;width:100%;text-align:center;padding-left:30px;font-family:"Pinyon Script",cursive;font-size:24px;color:#2b1a08}
.login label{position:absolute;font-size:12px;color:var(--ink);text-align:right;width:70px}
.login .field{position:absolute;left:80px;width:105px;height:18px;background:var(--white);border:1px solid #d9b37a}
.login-btn{top:65px;left:197px;width:52px;height:21px;border-radius:3px;background:linear-gradient(#2a2a2a,#000);color:var(--white);font-size:12px;display:flex;align-items:center;justify-content:center}

/* main frame */
.frame{top:147px;left:60px;width:703px;height:1053px;
  background:linear-gradient(90deg,var(--orange-deep),var(--orange) 12%,var(--orange-light) 50%,var(--orange) 88%,var(--orange-deep))}
.slider{top:162px;left:75px;width:671px;height:282px;border:3px solid var(--white);border-radius:6px;
  background:linear-gradient(100deg,#3a1206 0%,#7a2a10 22%,#c98a66 40%,#f2e2d8 58%,#f4d8d4 75%,#7a2010 100%)}
.dots{top:416px;left:536px;display:flex;gap:1px}
.dots i{width:16px;height:16px;border-radius:50%;background:#050505;display:block}
.dots i:first-child{background:#b03a06}

/* content card */
.card{top:470px;left:78px;width:507px;height:618px;background:var(--white);border-radius:3px;
  box-shadow:inset 0 0 22px rgba(120,140,170,.35)}
.h2{font-family:"Ubuntu",sans-serif;font-size:18px;color:var(--heading);font-weight:500}
.thumb{width:104px;height:75px;border:1px solid var(--orange);background:linear-gradient(90deg,#5a2018,#b04030 45%,#e8d8c0 60%,#6a6a70)}
.thumb::after{content:"";position:absolute;left:0;right:0;bottom:0;height:6px;background:#000}
.small{font-size:9px;line-height:11px;color:var(--ink);white-space:nowrap}
.more{font-size:9.5px;line-height:11px;color:var(--link-red);text-transform:uppercase}
.rule{height:0;border-top:1px dotted var(--rule)}
.para{font-size:8.5px;line-height:14.5px;color:var(--body-text);white-space:nowrap}
.bio-text{line-height:16.8px}
.bio-photo{top:906px;left:112px;width:160px;height:120px;
  background:linear-gradient(180deg,#2a7fd8 0%,#9cc8ee 38%,#b86a3a 45%,#3a3a3a 58%,#2a2a2a 100%)}

/* sidebar */
.side-h{font-family:"Ubuntu",sans-serif;font-size:13px;font-weight:400;color:var(--ink);text-transform:uppercase}
.quick{top:500px;left:619px;list-style:none;font-family:"Ubuntu",sans-serif;font-size:12px;line-height:19px}
.quick li::before{content:"\2192";margin-right:6px;font-weight:700}
.side-rule{left:598px;width:162px;border-top:1px dotted #6b3a10}
.news-input{top:692px;left:607px;width:143px;height:25px;background:var(--white);border:1px solid #bbb}
.subscribe{top:727px;left:610px;width:119px;height:28px;background:linear-gradient(#3a3a3a,#000);color:var(--white);font-family:"Ubuntu",sans-serif;font-size:13px;display:flex;align-items:center;justify-content:center}
.news-text{left:646px;font-size:8.5px;line-height:11.5px;color:var(--ink);white-space:nowrap}

.fans{top:941px;left:599px;width:162px;height:142px;background:var(--white);border-radius:3px}
.fans-bar{top:6px;left:2px;width:158px;height:15px;background:#4a5f8c;color:var(--white);font-family:"Ubuntu",sans-serif;font-size:10px;padding-left:3px;line-height:15px}
.fans-badge{top:27px;left:5px;width:20px;height:20px;background:#dfe6ef;border:1px solid #c2ccd8}
.fan-btn{top:37px;left:31px;width:63px;height:14px;border:1px solid #b9b9b9;background:#f2f2f2;font-size:7px;text-align:center;line-height:12px;color:#333}
.fans-grid{top:72px;left:5px;display:grid;grid-template-columns:repeat(5,27px);column-gap:4px;row-gap:4px}
.fan{width:27px;height:27px;background:#a9b0b8}
.fan-name{font-size:5px;text-align:center;color:#555;height:8px;line-height:8px}

/* footer */
.footer{top:1103px;left:76px;width:676px;height:97px;background:linear-gradient(180deg,var(--paper),#f3c06c 60%,var(--paper-dark))}
.copy{top:1146px;left:76px;width:640px;text-align:center;font-size:9.5px;color:var(--ink)}
</style>
</head>
<body>

<header>
  <div class="social abs" aria-label="Social links"><span></span><span></span><span></span><span></span><span></span></div>
  <div class="brand abs">Tavolin brise</div>
  <form class="login abs">
    <div class="login-title abs">Owner Login</div>
    <label style="top:47px;left:2px">Email :</label><span class="field" style="top:44px"></span>
    <label style="top:70px;left:4px">Password :</label><span class="field" style="top:67px"></span>
    <span class="login-btn abs">Login</span>
  </form>
</header>

<div class="frame abs"></div>

<div class="slider abs" role="img" aria-label="Birthday cake with pink candles beside two glasses of red wine"></div>
<div class="dots abs"><i></i><i></i><i></i><i></i><i></i></div>

<main class="card abs"></main>

<section aria-label="Latest Projects">
  <h2 class="h2 abs" style="top:496px;left:105px">Latest Projects</h2>
  <div class="thumb abs" style="top:535px;left:104px" role="img" aria-label="Hands working wood on a lathe"></div>
  <div class="thumb abs" style="top:535px;left:264px" role="img" aria-label="Hands working wood on a lathe"></div>
  <div class="thumb abs" style="top:535px;left:433px" role="img" aria-label="Hands working wood on a lathe"></div>
  <p class="small abs" style="top:618px;left:102px">Lorem ipsum dolor sit amet,<br>consectetuer adipiscing elit.<br>Lorem ipsum dolor sit amet,<br>consectetuer adipiscing elit.</p>
  <p class="small abs" style="top:618px;left:263px">Lorem ipsum dolor sit amet,<br>consectetuer adipiscing elit.<br>Lorem ipsum dolor sit amet,<br>consectetuer adipiscing elit.</p>
  <p class="small abs" style="top:618px;left:432px">Lorem ipsum dolor sit amet,<br>consectetuer adipiscing elit.<br>Lorem ipsum dolor sit amet,<br>consectetuer adipiscing elit.</p>
  <a class="more abs" style="top:670px;left:104px">View More</a>
  <a class="more abs" style="top:670px;left:264px">View More</a>
  <a class="more abs" style="top:670px;left:433px">View More</a>
</section>

<div class="rule abs" style="top:705px;left:94px;width:472px"></div>

<section aria-label="How About You">
  <h2 class="h2 abs" style="top:721px;left:110px">How About You</h2>
  <p class="para abs" style="top:755px;left:110px">Lorem ipsum dolor sit amet,consectetuer adipiscing elit. Lorem ipsum dolor sit amet,consectetuer adipiscing elit.<br>Lorem ipsum dolor sit amet,consectetuer adipiscing elit. Lorem ipsum dolor sit amet,consectetuer adipiscing<br>elit. Lorem ipsum dolor sit amet,consectetuer adipiscing elit. Lorem ipsum dolor sit amet,consectetuer adipiscing elit.<br>Lorem ipsum dolor sit amet,consectetuer adipiscing elit.</p>
  <a class="more abs" style="top:826px;left:503px">View More</a>
</section>

<div class="rule abs" style="top:857px;left:94px;width:472px"></div>

<section aria-label="Biography">
  <h2 class="h2 abs" style="top:869px;left:107px">Biography</h2>
  <div class="bio-photo abs" role="img" aria-label="Desert highway with yellow lines under a blue sky"></div>
  <p class="para bio-text abs" style="top:907px;left:285px">Lorem ipsum dolor sit amet,consectetuer adipiscing elit. Lorem ipsum<br>dolor sit amet,consectetuer adipiscing elit. Lorem ipsum<br>dolor sit amet,consectetuer adipiscing elit. Lorem ipsum dolor sit<br>amet,consectetuer adipiscing elit. Lorem ipsum dolor sit amet,<br>consectetuer adipiscing elit. Lorem ipsum dolor sit amet,consectetuer<br>adipiscing elit. Lorem ipsum dolor sit amet,consectetuer adipiscing elit.</p>
  <a class="more abs" style="top:1019px;left:289px">View More</a>
</section>

<aside>
  <h3 class="side-h abs" style="top:475px;left:612px">Quick Links</h3>
  <ul class="quick abs">
    <li>Home</li><li>About</li><li>Blog</li><li>News</li><li>Contact</li><li>Discography</li><li>Photo Gallery</li>
  </ul>
  <div class="side-rule abs" style="top:645px"></div>

  <h3 class="side-h abs" style="top:666px;left:608px">Newsletter</h3>
  <div class="news-input abs"></div>
  <div class="subscribe abs">Subscribe</div>
  <div class="side-rule abs" style="top:775px"></div>

  <h3 class="side-h abs" style="top:795px;left:608px">Latest News</h3>
  <svg class="abs" style="top:829px;left:608px" width="30" height="30" viewBox="0 0 30 30" aria-hidden="true">
    <rect x="1" y="3" width="28" height="26" rx="2" fill="#fff" stroke="#999"/>
    <rect x="1" y="3" width="28" height="7" fill="#3c9a3c"/>
    <rect x="13" y="17" width="5" height="5" fill="#c33"/>
  </svg>
  <p class="news-text abs" style="top:826px">Lorem ipsum dolor sit amet,<br>consectetuer adipiscing elit.<br>Lorem ipsum dolor .</p>
  <svg class="abs" style="top:886px;left:608px" width="30" height="30" viewBox="0 0 30 30" aria-hidden="true">
    <rect x="1" y="3" width="28" height="26" rx="2" fill="#fff" stroke="#999"/>
    <rect x="1" y="3" width="28" height="7" fill="#3c9a3c"/>
    <rect x="13" y="17" width="5" height="5" fill="#c33"/>
  </svg>
  <p class="news-text abs" style="top:883px">Lorem ipsum dolor sit amet,<br>consectetuer adipiscing elit.<br>Lorem ipsum dolor .</p>
  <div class="side-rule abs" style="top:933px"></div>

  <div class="fans abs">
    <div class="fans-bar abs">Fanpage</div>
    <div class="fans-badge abs"></div>
    <div class="fan-btn abs">Become a Fan</div>
    <div class="fans-grid abs">
      <div><div class="fan" role="img" aria-label="Fan profile photo"></div><div class="fan-name">Milo</div></div>
      <div><div class="fan" role="img" aria-label="Fan profile photo" style="background:#b9a48a"></div><div class="fan-name">Gita</div></div>
      <div><div class="fan" role="img" aria-label="Fan profile photo" style="background:#3a3a3a"></div><div class="fan-name">Marco</div></div>
      <div><div class="fan" role="img" aria-label="Fan profile photo" style="background:#7c8a78"></div><div class="fan-name">Bern</div></div>
      <div><div class="fan" role="img" aria-label="Fan profile photo" style="background:#8a8f95"></div><div class="fan-name">Kai</div></div>
      <div class="fan" role="img" aria-label="Fan profile photo" style="background:#c49a7a"></div>
      <div class="fan" role="img" aria-label="Fan profile photo" style="background:#9a6a5a"></div>
      <div class="fan" role="img" aria-label="Fan profile photo" style="background:#c8a46a"></div>
      <div class="fan" role="img" aria-label="Fan profile photo" style="background:#9a9a9a"></div>
      <div class="fan" role="img" aria-label="Fan profile photo" style="background:#b8b0a0"></div>
    </div>
  </div>
</aside>

<footer>
  <div class="footer abs"></div>
  <p class="copy abs">Copyright © Tavolinbrise, All Rights Reserved</p>
</footer>

</body>
</html>
```